Flyer-Design für Ankauf gebrauchter Bücher
Zielgruppe
Alle die Ihre gebrauchen Bücher verkaufen möchten.
Aufgabenstellung
Modern, farblich an alten Flyer und Logo anpassen
Achtung neue Adresse und Telefon Nr.
Buchhandel Markus Ehrlein
Alwin Tressel Straße 9
D-65417 Diez
Tel.: 06471/5829316

```html
<!DOCTYPE html>
<html lang="de">
<head>
<meta charset="utf-8">
<title>Flyer – Ankauf gebrauchter Bücher</title>
<link rel="stylesheet" href="https://fonts.googleapis.com/css2?family=Fira+Sans:wght@300;400;600;700&family=PT+Serif:wght@700&display=swap">
<style>
  :root {
    --magenta: #c1117b;
    --yellow: #f4c42a;
    --yellow-deep: #eaae18;
    --ink: #3a3a3a;
    --tag: #3d3d3d;
    --white: #ffffff;
  }
  html, body { margin: 0; padding: 0; overflow: hidden; background: var(--white); }
  .flyer {
    position: relative;
    width: 1200px; height: 849px;
    overflow: hidden;
    background: var(--white);
    font-family: "Fira Sans", Arial, sans-serif;
  }
  .photo-panel {
    position: absolute; left: 21px; top: 21px; width: 462px; height: 806px;
    background: radial-gradient(ellipse at 45% 45%, var(--yellow) 0%, var(--yellow-deep) 100%);
  }
  .color-panel {
    position: absolute; left: 483px; top: 21px; width: 694px; height: 806px;
    background: var(--magenta);
  }
  .headline {
    position: absolute; left: 528px; top: 96px; margin: 0;
    color: var(--white); font-weight: 600; font-size: 62px; line-height: 62px;
    letter-spacing: 0.5px;
  }
  .subline {
    position: absolute; left: 618px; top: 230px; margin: 0;
    color: var(--white); font-weight: 400; font-size: 23px; line-height: 28px;
  }
  .topics {
    position: absolute; left: 618px; top: 355px; width: 470px; margin: 0;
    color: var(--white); font-weight: 300; font-size: 15px; line-height: 27px;
  }
  .contact-bar {
    position: absolute; left: 382px; top: 551px; width: 795px; height: 139px;
    background: var(--white);
  }
  .brand {
    position: absolute; left: 40px; top: 46px;
    display: flex; align-items: center; gap: 14px;
  }
  .brand-square { width: 34px; height: 34px; background: var(--magenta); }
  .brand-name {
    color: var(--magenta); font-weight: 600; font-size: 30px; line-height: 1;
    white-space: nowrap;
  }
  .contact-details { position: absolute; left: 484px; top: 26px; }
  .web { color: var(--magenta); font-weight: 700; font-size: 25px; line-height: 28px; }
  .address { color: var(--ink); font-size: 16px; line-height: 22px; margin-top: 2px; }
  .hours { color: var(--magenta); font-weight: 700; font-size: 15.5px; line-height: 22px; margin-top: 4px; white-space: nowrap; }
  .phone-tag {
    position: absolute; left: 904px; top: 702px; width: 310px; height: 58px;
    background: var(--tag);
    transform: rotate(-6deg); transform-origin: left center;
    display: flex; align-items: center; gap: 8px; padding-left: 14px;
    box-sizing: border-box;
    color: var(--white); font-family: "PT Serif", Georgia, serif; font-weight: 700;
    font-size: 27px; white-space: nowrap;
  }
  .phone-tag svg { flex: none; }
  .visit-note {
    position: absolute; left: 524px; top: 724px; width: 340px; margin: 0;
    color: var(--white); font-weight: 300; font-size: 12px; line-height: 18px;
  }
</style>
</head>
<body>
  <main class="flyer">
    <div class="photo-panel" role="img" aria-label="Foto: junge Frau mit Brille hält einen großen Stapel Bücher vor gelbem Hintergrund"></div>
    <section class="color-panel"></section>

    <h1 class="headline">Wir kaufen Ihre<br>gebrauchten Bücher!</h1>
    <p class="subline">Sie bringen Ihre Bücher einfach vorbei<br>und wir machen Ihnen ein Angebot.</p>

    <p class="topics">Wir kaufen Bücher aus folgenden Themen:<br>
      Kinderbücher | Kochbücher | Bildbände | Biografien | Politik |<br>
      Taschenbücher | Fach- und Sachbücher | Technik | historische<br>
      und antiquarische Bücher | und viele weitere Themen …</p>

    <div class="contact-bar">
      <div class="brand">
        <span class="brand-square"></span>
        <span class="brand-name">Buchhandel Markus Ehrlein</span>
      </div>
      <div class="contact-details">
        <div class="web">buchhandel-ehrlein.de</div>
        <div class="address">Alwin-Tressel-Straße 9 · 65417 Diez</div>
        <div class="hours">Öffnungszeiten: Mo – Fr von 10 bis 17 Uhr</div>
      </div>
    </div>

    <div class="phone-tag">
      <svg width="24" height="24" viewBox="0 0 24 24" aria-hidden="true">
        <circle cx="12" cy="12" r="10.5" fill="none" stroke="#fff" stroke-width="1.8"/>
        <path d="M8.2 6.5c.6-.4 1.2-.3 1.5.2l1.1 1.9c.3.5.2 1-.2 1.3l-.8.6c.5 1.4 1.4 2.6 2.7 3.5l.7-.7c.4-.4.9-.4 1.3-.1l1.8 1.2c.5.3.6.9.2 1.4l-.7.9c-.5.6-1.3.8-2 .5-3.2-1.3-5.6-4-6.5-7.3-.2-.7.1-1.4.7-1.9z" fill="#fff"/>
      </svg>
      <span>06471 - 582 93 16</span>
    </div>

    <p class="visit-note">Bei großen Buch-Auflösungen kommen wir auch gerne zu Ihnen. Vereinbaren Sie gleich einen Termin mit uns.</p>
  </main>
</body>
</html>
```